Business card and stationnary for a doctor specialized in Orthopedic Surgery
Dr. Lucien R. Desrosiers
Business card and stationnary for a doctor specialized in Orthopedic Surgery - Medical
Creative Brief
Professional
Chirurgie Orthopédique
DO NOT LIST ADDRESS!
lucien@drdesrosiers-ortho.example
www.drdesrosiers-ortho.example
Concerning the business card, which matters most, please take into consideration the following: 1/ I need my name to be followed below it by my specialty and credentials, each on a separate line as follows Dr. Lucien R. Desrosiers Chirurgie Orthopédique Diplômé de l'UQX et l'Univ de Morvanne Ancien Interne des Hôpitaux de Clervaux 2/ I do not want any address to be listed 3/ my logo can be used either in the front but in a disrete way, or on the back as a watermark or in a corner....i will see which design is more clean and professional. 4/ Concerning the back of the business card, i need please TWO variations: - one without any text on the back except perhaps the logo or website, as u wish -and another one where you provide a place i can input four addresses myself later on ( you can write for now Hospital 1, address, tel...Hospital 2, address, tel , etc.. and i will edit them myself later on)

```html
<!DOCTYPE html>
<html lang="fr">
<head>
<meta charset="utf-8">
<title>Dr. Lucien R. Desrosiers – Business card options</title>
<link href="https://fonts.googleapis.com/css2?family=Open+Sans:wght@400;600;700&display=swap" rel="stylesheet">
<style>
  :root{
    --board:#262626;
    --board-light:#3a3a3a;
    --card:#ffffff;
    --blue:#1f5fb8;
    --blue-deep:#0d3a86;
    --blue-light:#3f86dd;
    --grey:#b9bec6;
    --ink:#4a4f57;
    --label:#d8d8d8;
  }
  *{box-sizing:border-box;margin:0;padding:0}
  html,body{width:1200px;height:611px;overflow:hidden}
  body{
    background:radial-gradient(ellipse at 50% 40%,var(--board-light),var(--board) 75%);
    font-family:"Open Sans",Arial,sans-serif;
    position:relative;
  }
  .option{position:absolute;width:360px}
  .option--1{left:34px;top:72px}
  .option--2{left:420px;top:72px}
  .option--3{left:804px;top:72px}
  .option--4{left:34px;top:334px}
  .option--5{left:420px;top:334px}
  .option--back{left:804px;top:334px}
  .option__label{text-align:center;color:var(--label);font-size:12px;margin-top:10px}
  .card{
    position:relative;width:360px;height:211px;background:var(--card);
    overflow:hidden;box-shadow:0 6px 14px rgba(0,0,0,.55);
  }
  .card__wave{position:absolute;inset:0;width:100%;height:100%}
  .card__body{position:absolute;inset:0;color:var(--ink)}
  .mark{
    position:absolute;left:0;right:0;text-align:center;
    font-weight:700;color:var(--blue);letter-spacing:1px;font-size:38px;line-height:1;
  }
  .mark--white{color:#fff}
  .name{font-weight:700;color:var(--blue);font-size:10px;text-align:center}
  .creds{font-size:6.5px;line-height:1.45;text-align:center;color:var(--ink)}
  .ident{position:absolute;left:0;right:0}
  .ident--light .name,.ident--light .creds{color:#fff}
  .contact{position:absolute;font-size:6.5px;line-height:1.9;color:#fff}
  .contact--dark{color:var(--ink)}
  .contact--row{display:flex;gap:12px}
  .contact__row{display:flex;align-items:center;gap:4px;white-space:nowrap}
  .icon{width:7px;height:7px;flex:none}
  .hospitals{position:absolute;font-size:6.5px;line-height:2.1;color:var(--ink)}
  .hospitals__row{border-bottom:1px solid var(--grey);width:70px}
  .divider{position:absolute;width:1px;background:var(--grey)}
  .divider--light{background:#fff;opacity:.6}
  .card--back{background:linear-gradient(160deg,var(--blue-light),var(--blue) 45%,var(--blue-deep))}
  .back__web{position:absolute;left:0;right:0;top:130px;text-align:center;color:#fff;font-size:7px}
</style>
</head>
<body>

<svg width="0" height="0" style="position:absolute" aria-hidden="true">
  <defs>
    <linearGradient id="waveBlue" x1="0" y1="0" x2="0" y2="1">
      <stop offset="0" stop-color="#3f86dd"/>
      <stop offset="1" stop-color="#0d3a86"/>
    </linearGradient>
    <symbol id="phone" viewBox="0 0 10 10"><path d="M2 1l2 2-1 1.2c.6 1.3 1.5 2.2 2.8 2.8L7 6l2 2-1.3 1.5C4.5 9.2 .8 5.5.5 2.3z" fill="currentColor"/></symbol>
    <symbol id="mail" viewBox="0 0 10 10"><rect x=".5" y="2" width="9" height="6" fill="none" stroke="currentColor"/><path d="M.5 2L5 5.6 9.5 2" fill="none" stroke="currentColor"/></symbol>
    <symbol id="globe" viewBox="0 0 10 10"><circle cx="5" cy="5" r="4.3" fill="none" stroke="currentColor"/><path d="M.7 5h8.6M5 .7c-2.4 2.6-2.4 6 0 8.6M5 .7c2.4 2.6 2.4 6 0 8.6" fill="none" stroke="currentColor" stroke-width=".7"/></symbol>
    <symbol id="pin" viewBox="0 0 10 10"><path d="M5 .5a3.3 3.3 0 0 1 3.3 3.3C8.3 6.3 5 9.5 5 9.5S1.7 6.3 1.7 3.8A3.3 3.3 0 0 1 5 .5z" fill="currentColor"/></symbol>
  </defs>
</svg>

<!-- Front 01 -->
<section class="option option--1">
  <div class="card">
    <svg class="card__wave" viewBox="0 0 360 211" preserveAspectRatio="none" aria-hidden="true">
      <path d="M0 140 C110 118 230 160 360 120 L360 211 L0 211Z" fill="url(#waveBlue)"/>
      <path d="M0 132 C110 108 230 150 360 110" fill="none" stroke="var(--grey)" stroke-width="4"/>
    </svg>
    <div class="card__body">
      <div class="mark" style="top:20px">LRD</div>
      <div class="ident" style="top:68px">
        <p class="name">Dr. Lucien R. Desrosiers</p>
        <p class="creds">Chirurgie Orthopédique<br>Diplômé de l'UQX et l'Univ de Morvanne<br>Ancien Interne des Hôpitaux de Clervaux</p>
      </div>
      <div class="contact" style="left:90px;top:150px">
        <div class="contact__row"><svg class="icon"><use href="#phone"/></svg>+(000) 3 555 214</div>
        <div class="contact__row"><svg class="icon"><use href="#mail"/></svg>lucien@drdesrosiers-ortho.example</div>
      </div>
      <div class="contact" style="left:232px;top:138px">
        <div class="contact__row">POBOX 118 Valmarre</div>
      </div>
    </div>
  </div>
  <p class="option__label">Front Card Option_01</p>
</section>

<!-- Front 02 -->
<section class="option option--2">
  <div class="card">
    <svg class="card__wave" viewBox="0 0 360 211" preserveAspectRatio="none" aria-hidden="true">
      <path d="M0 180 C120 165 240 195 360 172 L360 211 L0 211Z" fill="url(#waveBlue)"/>
      <path d="M0 174 C120 158 240 188 360 166" fill="none" stroke="var(--grey)" stroke-width="3"/>
    </svg>
    <div class="card__body">
      <div class="ident" style="top:26px">
        <p class="name">Dr. Lucien R. Desrosiers</p>
        <p class="creds">Chirurgie Orthopédique, Diplômé de l'UQX et l'Univ de Morvanne<br>Ancien Interne des Hôpitaux de Clervaux</p>
      </div>
      <div class="hospitals" style="left:60px;top:82px">
        <div class="hospitals__row">Hospital 1</div>
        <div class="hospitals__row">Hospital 2</div>
        <div class="hospitals__row">Hospital 3</div>
      </div>
      <div class="divider" style="left:142px;top:84px;height:58px"></div>
      <div class="contact contact--dark" style="left:152px;top:82px">
        <div class="contact__row">POBOX 118 Valmarre</div>
        <div class="contact__row"><svg class="icon"><use href="#phone"/></svg>+(000) 3 555 214</div>
        <div class="contact__row"><svg class="icon"><use href="#mail"/></svg>lucien@drdesrosiers-ortho.example</div>
        <div class="contact__row"><svg class="icon"><use href="#globe"/></svg>www.drdesrosiers-ortho.example</div>
      </div>
    </div>
  </div>
  <p class="option__label">Front Card Option_02</p>
</section>

<!-- Front 03 -->
<section class="option option--3">
  <div class="card">
    <svg class="card__wave" viewBox="0 0 360 211" preserveAspectRatio="none" aria-hidden="true">
      <path d="M0 118 C110 96 230 140 360 100 L360 211 L0 211Z" fill="url(#waveBlue)"/>
      <path d="M0 110 C110 86 230 130 360 90" fill="none" stroke="var(--grey)" stroke-width="4"/>
    </svg>
    <div class="card__body">
      <div class="mark" style="top:22px">LRD</div>
      <div class="ident ident--light" style="top:124px;left:24px;right:auto;width:170px">
        <p class="name">Dr. Lucien R. Desrosiers</p>
        <p class="creds">Chirurgie Orthopédique<br>Diplômé de l'UQX et l'Univ de Morvanne<br>Ancien Interne des Hôpitaux de Clervaux</p>
      </div>
      <div class="divider divider--light" style="left:200px;top:124px;height:52px"></div>
      <div class="contact" style="left:210px;top:120px">
        <div class="contact__row"><svg class="icon"><use href="#pin"/></svg>POBOX 118 Valmarre</div>
        <div class="contact__row"><svg class="icon"><use href="#phone"/></svg>+(000) 3 555 214</div>
        <div class="contact__row"><svg class="icon"><use href="#mail"/></svg>lucien@drdesrosiers-ortho.example</div>
        <div class="contact__row"><svg class="icon"><use href="#globe"/></svg>www.drdesrosiers-ortho.example</div>
      </div>
    </div>
  </div>
  <p class="option__label">Front Card Option_03</p>
</section>

<!-- Front 04 -->
<section class="option option--4">
  <div class="card">
    <svg class="card__wave" viewBox="0 0 360 211" preserveAspectRatio="none" aria-hidden="true">
      <path d="M0 108 C110 86 230 130 360 92 L360 211 L0 211Z" fill="url(#waveBlue)"/>
      <path d="M0 100 C110 76 230 120 360 82" fill="none" stroke="var(--grey)" stroke-width="4"/>
    </svg>
    <div class="card__body">
      <div class="ident" style="top:24px">
        <p class="name">Dr. Lucien R. Desrosiers</p>
        <p class="creds">Chirurgie Orthopédique<br>Diplômé de l'UQX et l'Univ de Morvanne<br>Ancien Interne des Hôpitaux de Clervaux</p>
      </div>
      <div class="contact" style="left:0;right:0;top:128px;text-align:center">
        <div>POBOX 118 Valmarre</div>
      </div>
      <div class="contact contact--row" style="left:62px;top:150px">
        <div class="contact__row"><svg class="icon"><use href="#phone"/></svg>+(000) 3 555 214</div>
        <div class="contact__row"><svg class="icon"><use href="#mail"/></svg>lucien@drdesrosiers-ortho.example</div>
      </div>
    </div>
  </div>
  <p class="option__label">Front Card Option_04</p>
</section>

<!-- Front 05 -->
<section class="option option--5">
  <div class="card">
    <svg class="card__wave" viewBox="0 0 360 211" preserveAspectRatio="none" aria-hidden="true">
      <path d="M0 160 C120 142 240 178 360 150 L360 211 L0 211Z" fill="url(#waveBlue)"/>
      <path d="M0 152 C120 132 240 170 360 140" fill="none" stroke="var(--grey)" stroke-width="4"/>
    </svg>
    <div class="card__body">
      <div class="mark" style="top:22px">LRD</div>
      <div class="ident" style="top:72px">
        <p class="name">Dr. Lucien R. Desrosiers</p>
        <p class="creds">Chirurgie Orthopédique<br>Diplômé de l'UQX et l'Univ de Morvanne<br>Ancien Interne des Hôpitaux de Clervaux</p>
      </div>
      <div class="contact" style="left:0;right:0;top:166px;text-align:center">
        <div>POBOX 118 Valmarre</div>
      </div>
      <div class="contact contact--row" style="left:40px;top:182px;gap:10px;font-size:6px">
        <div class="contact__row"><svg class="icon"><use href="#phone"/></svg>+(000) 3 555 214</div>
        <div class="contact__row"><svg class="icon"><use href="#globe"/></svg>www.drdesrosiers-ortho.example</div>
        <div class="contact__row"><svg class="icon"><use href="#mail"/></svg>lucien@drdesrosiers-ortho.example</div>
      </div>
    </div>
  </div>
  <p class="option__label">Front Card Option_05</p>
</section>

<!-- Back -->
<section class="option option--back">
  <div class="card card--back">
    <div class="card__body">
      <div class="mark mark--white" style="top:84px">LRD</div>
      <p class="back__web">www.drdesrosiers-ortho.example</p>
    </div>
  </div>
  <p class="option__label">Back card</p>
</section>

</body>
</html>
```